Lacrosse Magazine Ad
Pell9kin
Lacrosse Magazine Ad -
Creative Brief
This magazine ad is about our non-for-profit organization Pell9kin. We want this Pell9kin ad to go along with our "Goal" Campaign. The first 2 ads from this campaign are attached. Pell9kin is an organization that spreads the game of lacrosse throughout Long Island, NY to underprivileged areas that don't have the sport of lacrosse. Pell9kin is a growing project and is always welcoming to those who are willing to help spread the game of lacrosse.
Anyone who is interested in lacrosse and cares about helping spread the game of lacrosse.
**Must say that Pell9kin is the non-for-profit side of Under the Bright Harbor Sky Lacrosse. -Pell9kin logo (attached) -Short and simple description of Pell9kin -Our website - www.pell9kin.example -Have a similar look to our 2 previous ads

```html
<!DOCTYPE html>
<html lang="en">
<head>
<meta charset="utf-8">
<title>Pell9kin – All Out All The Time</title>
<link rel="stylesheet" href="https://fonts.googleapis.com/css2?family=Bebas+Neue&family=Open+Sans:wght@400;600&display=swap">
<style>
  :root {
    --ink: #050505;
    --deep: #1c1c1c;
    --mid: #4a4a4a;
    --white: #ffffff;
    --sky: #7fa6cf;
    --body: #e6e6e6;
  }
  html, body {
    margin: 0;
    padding: 0;
    width: 1200px;
    height: 871px;
    overflow: hidden;
    background: var(--ink);
  }
  .ad {
    position: relative;
    width: 1200px;
    height: 871px;
    overflow: hidden;
    background: radial-gradient(ellipse at 30% 20%, var(--mid) 0%, var(--deep) 35%, var(--ink) 75%);
    font-family: "Open Sans", Arial, sans-serif;
  }
  .player-collage {
    position: absolute;
    left: 0;
    top: 120px;
    width: 640px;
    height: 580px;
    background: radial-gradient(ellipse at 35% 45%, rgba(150,150,150,0.45) 0%, rgba(70,70,70,0.3) 40%, rgba(0,0,0,0) 72%);
  }
  .stick-head {
    position: absolute;
    left: 600px;
    top: 470px;
    width: 600px;
    height: 401px;
    background: radial-gradient(ellipse at 45% 65%, rgba(200,200,200,0.55) 0%, rgba(110,110,110,0.35) 35%, rgba(0,0,0,0) 70%);
  }
  .headline {
    position: absolute;
    left: 233px;
    top: 206px;
    margin: 0;
    font-family: "Bebas Neue", Impact, sans-serif;
    font-weight: 400;
    font-size: 134px;
    line-height: 0.9;
    letter-spacing: 1px;
    color: var(--white);
  }
  .headline .accent { color: var(--sky); }
  .brand {
    position: absolute;
    right: 70px;
    top: 92px;
    display: flex;
    align-items: center;
    gap: 14px;
  }
  .brand-name {
    font-family: "Open Sans", Arial, sans-serif;
    font-weight: 600;
    font-size: 72px;
    line-height: 1;
    color: var(--white);
  }
  .brand-dot {
    width: 20px;
    height: 20px;
    border-radius: 50%;
    background: var(--sky);
  }
  .copy {
    position: absolute;
    left: 24px;
    top: 704px;
    width: 790px;
    color: var(--body);
    font-size: 17px;
    line-height: 1.27;
  }
  .copy p { margin: 0 0 14px; }
  .copy p:last-child { margin-bottom: 0; }
  .copy strong { font-weight: 600; color: var(--white); }
  .contact {
    position: absolute;
    right: 20px;
    top: 784px;
    text-align: right;
    color: var(--white);
  }
  .contact-lead {
    margin: 0;
    font-size: 20px;
  }
  .contact-url {
    margin: 4px 0 0;
    font-size: 25px;
    font-weight: 600;
    color: var(--sky);
  }
</style>
</head>
<body>
  <main class="ad">
    <div class="player-collage" role="img" aria-label="Faded collage of lacrosse players in action"></div>
    <div class="stick-head" role="img" aria-label="Close-up of a lacrosse stick head cradling a ball"></div>

    <div class="brand">
      <span class="brand-name">Pell9kin</span>
      <span class="brand-dot"></span>
    </div>

    <h1 class="headline">
      <span>ALL</span> <span class="accent">OUT</span><br>
      <span>ALL</span> <span class="accent">THE TIME</span>
    </h1>

    <section class="copy">
      <p>Pell9kin is the non-for-profit side of Under the Bright Harbor Sky (UBHS) Lacrosse. We spread the game of lacrosse throughout Long Island, NY to underprivileged areas that don't have the sport, bringing sticks, clinics and coaches to kids who have never played.</p>
      <p>To learn more and to find out how you can help spread the game, go to <strong>pell9kin.example</strong> Volunteers and donors are always welcome.</p>
    </section>

    <div class="contact">
      <p class="contact-lead">For more information visit</p>
      <p class="contact-url">www.pell9kin.example</p>
    </div>
  </main>
</body>
</html>
```